Business Card and Logo Color Scheme Design Contest

We are starting a new company called Lone Ridge Structural Partners and already have a logo however, the colors for the logo itself are not final and COULD be changed. I'm hoping to move AWAYfrom the gold color in the card and the logo as it seems a bit outdated. What we need help with is to find what our business color scheme will be, and then incorporate those colors into both the logo and the business card design itself. We also want to make sure we are known as "LRS" so in the future we can just refer to ourselves as "LRS" and not Lone Ridge Structural Partners. That being said, I would like to make a slight change to the logo to somehow include the letters "LRS." The logo used in the front of the card design MUST ALSO include the words "Firm No. 64307" within the logo. My vision is for the front of the card to have the information shown in the attached image. For the back of the card, I'm hoping to have something very simple. I'm envisioning a solid color with either the website (www.bridgemarkplans.com) and a simplified version of the logo. I've attached an example but I'm looking for a complete redesign. I'm looking for a slick, modern and simple design.

Industry/Entity Type

Civil Engineer

Contact Information for Business Card

Logo
Firm No. 64307
Daniel Whitcombe, PE
Chief Operating Officer
Email:mholloway@bridgemarkplans.com
Ph: 936.555.0142 | D: 936.555.0178 | M:210.555.0263
4187 W. Kellingham, Conroe, Texas 77301
www.bridgemarkplans.com

Requirements
Must have
• Logo
Contact Info
Nice to have
• "LRS" Incorporated in the design
Should not have
• The current color scheme

```html
<!DOCTYPE html>
<html lang="en">
<head>
<meta charset="utf-8">
<title>Lone Ridge Structural Partners — Business Card &amp; Logo</title>
<link rel="stylesheet" href="https://fonts.googleapis.com/css2?family=Marcellus&family=Tinos&display=swap">
<style>
  :root {
    --page: #ffffff;
    --card-light: #eeeeef;
    --card-dark: #54575c;
    --ink: #54575c;
    --ink-light: #ffffff;
    --mark-font: "Marcellus", serif;
    --text-font: "Tinos", "Times New Roman", serif;
  }
  * { margin: 0; padding: 0; box-sizing: border-box; }
  html, body {
    width: 1200px;
    height: 1114px;
    overflow: hidden;
    background: var(--page);
  }
  .canvas {
    position: relative;
    width: 1200px;
    height: 1114px;
  }
  .card {
    position: absolute;
    left: 57px;
    top: 53px;
    width: 1086px;
    height: 311px;
    display: flex;
  }
  .card-front {
    position: relative;
    width: 543px;
    height: 100%;
    background: var(--card-light);
  }
  .card-contact {
    position: relative;
    width: 543px;
    height: 100%;
    background: var(--card-dark);
    color: var(--ink-light);
    font-family: var(--text-font);
    padding: 38px 0 0 45px;
  }
  .wordmark {
    position: absolute;
    left: 0;
    width: 100%;
    text-align: center;
    color: var(--ink);
  }
  .wordmark-letters {
    display: block;
    font-family: var(--mark-font);
    font-weight: 400;
    line-height: 1;
  }
  .wordmark-firm {
    display: block;
    font-family: var(--text-font);
    line-height: 1;
  }
  .card-front .wordmark { top: 47px; }
  .card-front .wordmark-letters {
    font-size: 114px;
    letter-spacing: 22px;
    padding-left: 22px;
  }
  .card-front .wordmark-firm {
    font-size: 17.5px;
    margin-top: 22px;
  }
  .contact-name {
    font-size: 21px;
    line-height: 1.2;
  }
  .contact-title {
    font-size: 17px;
    line-height: 1.3;
    margin-top: 1px;
  }
  .contact-details {
    position: absolute;
    left: 45px;
    top: 192px;
    font-size: 19.2px;
    line-height: 28px;
  }
  .logo-display {
    top: 454px;
  }
  .logo-display .wordmark-letters {
    font-size: 340px;
    letter-spacing: 80px;
    padding-left: 80px;
  }
  .logo-display .wordmark-firm {
    font-size: 53px;
    margin-top: 96px;
  }
</style>
</head>
<body>
  <main class="canvas">
    <section class="card" aria-label="Business card">
      <div class="card-front">
        <div class="wordmark">
          <span class="wordmark-letters">LRS</span>
          <span class="wordmark-firm">"Engineering Firm No. 64307 "</span>
        </div>
      </div>
      <div class="card-contact">
        <p class="contact-name">Daniel Whitcombe, PE</p>
        <p class="contact-title">Chief Operating Officer</p>
        <div class="contact-details">
          <p>Email: dwhitcombe@bridgemarkplans.com</p>
          <p>Ph: 936.555.0142 - D: 936.555.0178 - M: 210.555.0263</p>
          <p>4187 W. Kellingham, Conroe, Texas 77301</p>
        </div>
      </div>
    </section>

    <section class="wordmark logo-display" aria-label="Logo">
      <span class="wordmark-letters">LRS</span>
      <span class="wordmark-firm">"Engineering Firm No. 64307 "</span>
    </section>
  </main>
</body>
</html>
```